Professional Home Buyer business card needed

I need a pretty straight forward business card designed. We help people that NEED to sell their homes solve problems. We perform all types of Real Estate transactions including flip, wholesale, investment, rental property and multi family. The card will mainly be used to give to prospective Sellers but will also be given to Real Estate Investors as well. It should professional and very easy to read, most clients are older people.

Target Market(s)

Distressed home sellers as well as Real Estate investors

Industry/Entity Type

Real Estate

Contact Information for Business Card

should be a professional layout

Colors
ec1f27
ffffff
000000

Requirements
Must have
• Large logo on back and smaller one on front. should utilize Red, white, and black.
• I am thinking of using a soft touch coating on the card so keep that in mind.
• Contact info should be very easy to read, think older clients.
Nice to have
• I would like to see a design with rounded corners on the card
Should not have
• pictures of homes or other home graphics.

```html
<!DOCTYPE html>
<html lang="en">
<head>
<meta charset="utf-8">
<title>Keystone Home Buyers – Business Card</title>
<link rel="stylesheet" href="https://fonts.googleapis.com/css2?family=Cormorant+Garamond:wght@600&family=Montserrat:wght@800&family=Questrial&display=swap">
<style>
  :root {
    --red: #ec1f27;
    --white: #ffffff;
    --black: #000000;
    --backdrop: #bdbdbd;
    --band-dark: #7c7c7c;
    --band-mid: #939393;
    --band-light: #c9c9c9;
    --silver-light: #e4e4e4;
    --silver-mid: #bcbcbc;
    --silver-dark: #9a9a9a;
  }
  * { margin: 0; padding: 0; box-sizing: border-box; }
  html, body { width: 1200px; height: 1200px; overflow: hidden; }
  body { background: var(--backdrop); position: relative; font-family: "Questrial", sans-serif; }

  .card {
    position: absolute;
    left: 179px;
    width: 840px;
    height: 480px;
    background: var(--black);
    overflow: hidden;
    box-shadow: 0 6px 14px rgba(0,0,0,0.35);
  }
  .card--front { top: 74px; }
  .card--back { top: 631px; }

  .brand-name {
    font-family: "Montserrat", sans-serif;
    font-weight: 800;
    color: var(--white);
    text-align: center;
    text-transform: uppercase;
  }
  .card--front .brand-name {
    position: absolute;
    left: 0; right: 0; top: 178px;
    font-size: 58px;
    letter-spacing: 6px;
    line-height: 1.1;
  }
  .card--front .brand-name span { display: block; font-size: 34px; letter-spacing: 12px; }

  .back-stripes { position: absolute; left: 0; top: 0; }

  .holder {
    position: absolute;
    left: 380px; width: 340px; top: 68px;
    text-align: center;
    color: var(--white);
    font-family: "Cormorant Garamond", serif;
    font-weight: 600;
  }
  .holder__name { font-size: 58px; line-height: 1; }
  .holder__title { font-size: 38px; line-height: 1.1; }

  .contact-band {
    position: absolute;
    left: 0; top: 255px; width: 840px; height: 164px;
    background: linear-gradient(95deg, var(--band-dark) 0%, var(--band-mid) 55%, var(--band-light) 78%, var(--silver-mid) 100%);
  }
  .contact-row {
    position: absolute;
    left: 93px;
    color: var(--white);
    text-shadow: 0 1px 2px rgba(0,0,0,0.7), 0 0 1px rgba(0,0,0,0.6);
  }
  .contact-row--phone { top: 12px; font-size: 30px; letter-spacing: 1px; }
  .contact-row--email { top: 50px; font-size: 28px; }
  .contact-row--address { top: 88px; font-size: 19px; line-height: 23px; }
  .contact-icon { position: absolute; filter: drop-shadow(0 1px 1px rgba(0,0,0,0.6)); }

  .contact-band .brand-name {
    position: absolute;
    left: 600px; width: 210px; top: 50px;
    font-size: 22px;
    letter-spacing: 2px;
    line-height: 1.25;
    color: var(--black);
  }
  .contact-band .brand-name span { display: block; font-size: 14px; letter-spacing: 4px; }

  .web-bar {
    position: absolute;
    left: 0; top: 419px; width: 840px; height: 38px;
    background: linear-gradient(100deg, var(--silver-dark) 0%, var(--white) 25%, var(--silver-mid) 50%, var(--white) 75%, var(--silver-dark) 100%);
    text-align: center;
    font-size: 27px;
    line-height: 38px;
    color: var(--black);
  }
  .corner-accent { position: absolute; right: 0; bottom: 0; }
</style>
</head>
<body>

<section class="card card--front" aria-label="Card front">
  <h1 class="brand-name">Keystone<span>Home Buyers</span></h1>
</section>

<section class="card card--back" aria-label="Card back">
  <svg class="back-stripes" width="840" height="255" viewBox="0 0 840 255" aria-hidden="true">
    <polygon points="601,255 840,78 840,117 660,255" fill="var(--white)"/>
    <polygon points="640,255 840,117 840,255" fill="var(--red)"/>
  </svg>

  <div class="holder">
    <div class="holder__name">Daniel Harlow</div>
    <div class="holder__title">— President —</div>
  </div>

  <div class="contact-band">
    <svg class="contact-icon" style="left:45px;top:20px" width="24" height="24" viewBox="0 0 24 24" aria-hidden="true">
      <path d="M6.6 10.8c1.4 2.8 3.8 5.1 6.6 6.6l2.2-2.2c.3-.3.7-.4 1-.2 1.1.4 2.300.6 3.6.6.6 0 1 .4 1 1V20c0 .6-.4 1-1 1C10.6 21 3 13.4 3 4c0-.6.4-1 1-1h3.5c.6 0 1 .4 1 1 0 1.3.2 2.5.6 3.6.1.3 0 .7-.2 1z" fill="var(--white)"/>
    </svg>
    <div class="contact-row contact-row--phone">555-014-2287</div>

    <svg class="contact-icon" style="left:44px;top:55px" width="28" height="26" viewBox="0 0 28 26" aria-hidden="true">
      <path d="M2 10 L14 2 L26 10 V24 H2 Z M2 10 L14 18 L26 10 M2 24 L11 16 M26 24 L17 16" fill="none" stroke="var(--white)" stroke-width="2"/>
    </svg>
    <div class="contact-row contact-row--email">daniel@plainshomesforcash.com</div>

    <svg class="contact-icon" style="left:34px;top:95px" width="48" height="52" viewBox="0 0 48 52" aria-hidden="true">
      <path d="M24 2a11 11 0 0 0-11 11c0 8 11 20 11 20s11-12 11-20A11 11 0 0 0 24 2zm0 15a4.5 4.5 0 1 1 0-9 4.5 4.5 0 0 1 0 9z" fill="var(--white)"/>
      <path d="M3 48 L12 38 L20 42 L28 36 L36 42 L45 38 L40 48 L32 44 L24 49 L16 44 Z" fill="none" stroke="var(--white)" stroke-width="2"/>
    </svg>
    <div class="contact-row contact-row--address">Optional address:<br>P.O. Box 82<br>Linwood, KS 67000</div>

    <div class="brand-name">Keystone<span>Home Buyers</span></div>
  </div>

  <div class="web-bar">www.plainshomesforcash.com</div>

  <svg class="corner-accent" width="32" height="23" viewBox="0 0 32 23" aria-hidden="true">
    <polygon points="0,0 32,0 32,23" fill="var(--red)"/>
  </svg>
</section>

</body>
</html>
```